Business Card Design - Law Firm

I need a business card design. I have attached a picture of the law firm's website and logo. The business card design should be consistent with those pictures. There should be a place for the employee name, employee job title, telephone number, facsimile number, address, website url, and email address for each employee.
Industry/Entity Type
Business

```html
<!DOCTYPE html>
<html lang="en">
<head>
<meta charset="UTF-8">
<title>Wexford Law – Business Card</title>
<link href="https://fonts.googleapis.com/css2?family=Libre+Baskerville:ital,wght@0,400;1,700&display=swap" rel="stylesheet">
<style>
  :root {
    --page-bg: #f2f2ee;
    --card-olive: #7a7d5e;
    --tab-cream: #e6e5bd;
    --brand-gold: #a89a1d;
    --mark-dark: #1f2120;
    --rule-grey: #6b6b5a;
    --text-light: #f7f6ea;
  }
  html, body {
    margin: 0;
    padding: 0;
    width: 1200px;
    height: 819px;
    overflow: hidden;
    background: var(--page-bg);
  }
  .card {
    position: absolute;
    left: 60px;
    top: 85px;
    width: 1080px;
    height: 648px;
    background: var(--card-olive);
    overflow: hidden;
  }
  .card-shapes {
    position: absolute;
    inset: 0;
    width: 1080px;
    height: 648px;
  }
  .brand-name {
    position: absolute;
    left: 293px;
    top: 84px;
    margin: 0;
    font-family: "Libre Baskerville", serif;
    font-weight: 400;
    font-size: 46px;
    line-height: 1;
    color: var(--brand-gold);
    white-space: nowrap;
  }
  .employee {
    position: absolute;
    right: 124px;
    top: 84px;
    text-align: right;
    font-family: "Libre Baskerville", serif;
    font-style: italic;
    font-weight: 700;
    color: var(--text-light);
  }
  .employee-name {
    margin: 0;
    font-size: 29px;
    line-height: 1.2;
    margin-right: -8px;
  }
  .employee-title {
    margin: 6px 0 0;
    font-size: 26px;
    line-height: 1.2;
  }
  .contact {
    position: absolute;
    top: 535px;
    margin: 0;
    font-family: "Libre Baskerville", serif;
    font-style: italic;
    font-weight: 700;
    font-size: 25px;
    line-height: 41px;
    letter-spacing: 1px;
    color: var(--text-light);
  }
  .contact-col-1 { left: 81px; }
  .contact-col-2 { left: 345px; }
  .contact-col-3 { left: 653px; }
  .contact span { display: block; }
</style>
</head>
<body>
  <section class="card" aria-label="Wexford Law business card">
    <svg class="card-shapes" viewBox="0 0 1080 648" aria-hidden="true">
      <defs>
        <filter id="tab-shadow" x="-10%" y="-10%" width="130%" height="130%">
          <feDropShadow dx="10" dy="10" stdDeviation="10" flood-color="#2f3023" flood-opacity="0.55"/>
        </filter>
      </defs>
      <path class="brand-tab"
            d="M22 7 L672 7 C600 90 592 230 672 315 L24 308 Z"
            fill="var(--tab-cream)" filter="url(#tab-shadow)"/>
      <circle class="brand-dot" cx="176" cy="126" r="58" fill="var(--mark-dark)"/>
      <line class="brand-divider" x1="281" y1="31" x2="281" y2="221"
            stroke="var(--rule-grey)" stroke-width="1.5"/>
    </svg>

    <p class="brand-name">Wexford Law</p>

    <div class="employee">
      <p class="employee-name">Employee Name</p>
      <p class="employee-title">Job Title</p>
    </div>

    <p class="contact contact-col-1"><span>Phone:</span><span>e-mail:</span></p>
    <p class="contact contact-col-2"><span>Facsimile:</span><span>website:</span></p>
    <p class="contact contact-col-3"><span>Address:</span></p>
  </section>
</body>
</html>
```